Flaschenetiketten-Design in rechteckiger Grundform für Biermanufaktur
Der Kontakt war sehr professionell und angenehm. Wir wurden hilfreich beraten. Auf unser Feedback haben wir in kurzer Zeit jeweils neue Entwürfe erhalten. Die Zusammenarbeit und der Service war deutlich über unseren Vorstellungen. Wir können KorvaneDeck nur weiterempfehlen!
Zielgruppe
Wir repräsentieren eine Bier-Manufaktur in der Gründungsphase und sind auf der Suche nach einem Designvorschlag für die Flaschenetiketten.
Unsere Zielgruppe sind Liebhaber, die auf der Suche nach dem Speziellen und Lokalen sind. Der Biergenuss abseits des Massenmarktes soll im Entwurf sichtbar/transportiert werden. Die Bier-Manufaktur steht zeitgleich für Trend-Kreationen mit bodenständigem Ursprung.
Aufgabenstellung
Die Herkunft der Gründer Familie aus dem Schweizer Kanton Simplon soll im Vordergrund stehen, hierzu bitte das Familienwappen / einzelne Elemente siehe Dateiupload berücksichtigen.
Das Etikett soll eine rechteckige Grundform haben.
Folgende Angaben sollen sich im Etikett wiederfinden:
- Biersorte: 'Lager' (zukünftig soll es möglich sein, Biersorte auf dem Etikett zu wechseln)
Brand: 'Mostly Grafun'
'Biermanufaktur Walliser Ursprungs'
Die Schrift soll klar und nicht zu verspielt sein.

```html
<!DOCTYPE html>
<html lang="de">
<head>
<meta charset="utf-8">
<title>Mostly Grafun – Etikett</title>
<link rel="stylesheet" href="https://fonts.googleapis.com/css2?family=League+Spartan:wght@400;500;600&display=swap">
<style>
  :root {
    --paper: #ffffff;
    --stage: #262626;
    --label: #2d2d2d;
    --label-deep: #262626;
    --ink: #ffffff;
    --silver-hi: #f2f2f2;
    --silver-mid: #a9a9a9;
    --silver-lo: #5e5e5e;
    --amber-hi: #b26a1f;
    --amber-lo: #4a2406;
  }
  * { margin: 0; padding: 0; box-sizing: border-box; }
  html, body { width: 844px; height: 1200px; overflow: hidden; }
  body {
    position: relative;
    background: var(--paper);
    font-family: "League Spartan", "Montserrat", sans-serif;
    color: var(--ink);
  }
  .board-top { position: absolute; left: 0; top: 0; width: 844px; height: 517px; background: var(--paper); }
  .board-bottom { position: absolute; left: 0; top: 517px; width: 844px; height: 683px; background: var(--stage); }

  .silver-frame {
    background: linear-gradient(135deg, var(--silver-lo), var(--silver-hi) 35%, var(--silver-mid) 60%, var(--silver-hi) 85%, var(--silver-lo));
  }

  /* Front label */
  .front-label {
    position: absolute; width: 400px; height: 444px; padding: 5px;
    box-shadow: 0 6px 14px rgba(0,0,0,.35);
  }
  .board-top .front-label { left: 213px; top: 36px; }
  .front-label__face {
    position: relative; width: 100%; height: 100%;
    background: var(--label);
    overflow: hidden;
  }
  .front-label__backdrop {
    position: absolute; left: 8px; top: 30px; width: 300px; height: 400px;
    border-radius: 40% 45% 20% 30%;
    background: radial-gradient(ellipse at 50% 50%, #333333, var(--label) 70%);
  }
  .crest {
    display: block;
    background: linear-gradient(160deg, var(--silver-hi), var(--silver-mid) 55%, var(--silver-lo));
    clip-path: polygon(0 0, 100% 0, 100% 78%, 50% 100%, 0 78%);
  }
  .front-label .crest { position: absolute; left: 122px; top: 31px; width: 147px; height: 180px; }
  .brand-name {
    position: absolute; left: 0; right: 0; top: 262px;
    text-align: center; font-weight: 500; font-size: 62px; line-height: 56px;
    letter-spacing: 2px;
  }
  .brand-origin {
    position: absolute; left: 0; right: 0; top: 394px;
    text-align: center; font-weight: 600; font-size: 10px; letter-spacing: 1.4px;
  }

  /* Neck labels */
  .neck-label { position: absolute; left: 29px; width: 796px; height: 68px; padding: 2px; }
  .neck-label--info { top: 16px; }
  .neck-label--blank { top: 100px; }
  .neck-label__face { position: relative; width: 100%; height: 100%; background: var(--label-deep); }
  .neck-label .crest { position: absolute; top: 5px; width: 46px; height: 54px; }
  .neck-label .crest--left { left: 5px; }
  .neck-label .crest--right { right: 5px; }
  .neck-label__title {
    position: absolute; left: 67px; top: 8px;
    font-weight: 500; font-size: 31px; letter-spacing: 2.5px; line-height: 1;
  }
  .neck-label__gravity { position: absolute; left: 68px; top: 47px; font-size: 10px; letter-spacing: 1px; font-weight: 500; }
  .neck-label__abv { position: absolute; left: 326px; top: 47px; font-size: 10px; letter-spacing: 1px; font-weight: 500; }
  .brew-facts {
    position: absolute; left: 412px; top: 10px; width: 310px;
    font-size: 10px; font-weight: 500; letter-spacing: 1px; line-height: 14px;
  }
  .brew-facts__row { display: flex; justify-content: space-between; }
  .brew-facts__row--gap { margin-top: 6px; }

  /* Bottles */
  .bottle { position: absolute; top: 197px; width: 108px; height: 469px; }
  .bottle--one { left: 183px; }
  .bottle--two { left: 368px; }
  .bottle--three { left: 553px; }
  .bottle__glass {
    position: absolute; inset: 0;
    border-radius: 30px 30px 8px 8px / 160px 160px 8px 8px;
    background: linear-gradient(90deg, var(--amber-lo), var(--amber-hi) 35%, #8a4b12 65%, var(--amber-lo));
  }
  .bottle .front-label {
    left: -1px; top: 247px;
    transform: scale(.2725); transform-origin: 0 0;
    box-shadow: none;
  }
</style>
</head>
<body>
  <section class="board-top">
    <div class="front-label silver-frame">
      <div class="front-label__face">
        <div class="front-label__backdrop" role="img" aria-label="Faint heraldic eagle decoration"></div>
        <span class="crest" role="img" aria-label="Silver family coat of arms"></span>
        <div class="brand-name">MOSTLY<br>GRAFUN</div>
        <div class="brand-origin">BIERMANUFAKTUR HALDERWEG BRENZACH</div>
      </div>
    </div>
  </section>

  <section class="board-bottom">
    <div class="neck-label neck-label--info silver-frame">
      <div class="neck-label__face">
        <span class="crest crest--left" role="img" aria-label="Silver family coat of arms"></span>
        <div class="neck-label__title">MOSTLY GRAFUN</div>
        <div class="neck-label__gravity">STAMMWÜRZE 12P</div>
        <div class="neck-label__abv">4.5VOL.%</div>
        <div class="brew-facts">
          <div class="brew-facts__row"><span>GEBRAUT: 31.01.2019</span><span>ABGEFÜLLT: 12.02.2019</span></div>
          <div>REZEPT. SUDKESSELUNDKORN</div>
          <div class="brew-facts__row--gap">MALZMISCHUNG: PILSNER, CARALUX, CARAKLAR</div>
        </div>
        <span class="crest crest--right" role="img" aria-label="Silver family coat of arms"></span>
      </div>
    </div>

    <div class="neck-label neck-label--blank silver-frame">
      <div class="neck-label__face">
        <span class="crest crest--left" role="img" aria-label="Silver family coat of arms"></span>
        <span class="crest crest--right" role="img" aria-label="Silver family coat of arms"></span>
      </div>
    </div>

    <div class="bottle bottle--one">
      <div class="bottle__glass" role="img" aria-label="Amber swing-top beer bottle"></div>
      <div class="front-label silver-frame">
        <div class="front-label__face">
          <div class="front-label__backdrop" role="img" aria-label="Faint heraldic eagle decoration"></div>
          <span class="crest" role="img" aria-label="Silver family coat of arms"></span>
          <div class="brand-name">MOSTLY<br>GRAFUN</div>
          <div class="brand-origin">BIERMANUFAKTUR HALDERWEG BRENZACH</div>
        </div>
      </div>
    </div>

    <div class="bottle bottle--two">
      <div class="bottle__glass" role="img" aria-label="Amber swing-top beer bottle"></div>
      <div class="front-label silver-frame">
        <div class="front-label__face">
          <div class="front-label__backdrop" role="img" aria-label="Faint heraldic eagle decoration"></div>
          <span class="crest" role="img" aria-label="Silver family coat of arms"></span>
          <div class="brand-name">MOSTLY<br>GRAFUN</div>
          <div class="brand-origin">BIERMANUFAKTUR HALDERWEG BRENZACH</div>
        </div>
      </div>
    </div>

    <div class="bottle bottle--three">
      <div class="bottle__glass" role="img" aria-label="Amber swing-top beer bottle"></div>
      <div class="front-label silver-frame">
        <div class="front-label__face">
          <div class="front-label__backdrop" role="img" aria-label="Faint heraldic eagle decoration"></div>
          <span class="crest" role="img" aria-label="Silver family coat of arms"></span>
          <div class="brand-name">MOSTLY<br>GRAFUN</div>
          <div class="brand-origin">BIERMANUFAKTUR HALDERWEG BRENZACH</div>
        </div>
      </div>
    </div>
  </section>
</body>
</html>
```